Cannabis & Shroom Informative

Online Blog/Informative website design
Example site: https://herbalnookwest.com/

I will need the Ad space as well.

Target Market(s)

Cannabis and (psyho) Mushroom Users

Number of Pages Required

1 page

Colors

```html
<!DOCTYPE html>
<html lang="en">
<head>
<meta charset="utf-8">
<title>Verdant Notes – Cannabis &amp; Mushroom Information</title>
<link rel="stylesheet" href="https://fonts.googleapis.com/css2?family=Barlow:wght@400;500;600;700&family=Montserrat:wght@500;600;700&family=Oswald:wght@400;600&display=swap">
<style>
:root{
  --green:#6ab72c;
  --green-dark:#4f9a1c;
  --ink:#1d1d1d;
  --text:#3a3a3a;
  --muted:#8a8a8a;
  --rule:#bdbdbd;
  --band:#f3eff0;
  --footer:#1e1e1e;
  --footer-rule:#3a3a3a;
  --white:#ffffff;
  --orange:#f27a12;
  --soil:#2b2118;
}
*{box-sizing:border-box;margin:0;padding:0}
html,body{width:1200px;height:4267px;overflow:hidden}
body{font-family:"Barlow",sans-serif;color:var(--text);background:var(--white);position:relative}
a{color:inherit;text-decoration:none}

/* header */
.site-header{position:absolute;left:0;top:0;width:1200px;height:103px;background:var(--white)}
.brand{position:absolute;left:131px;top:24px;display:flex;align-items:center;gap:12px}
.brand-dot{width:40px;height:40px;border-radius:50%;background:var(--green)}
.brand-name{font-family:"Montserrat",sans-serif;font-weight:700;font-size:28px;color:var(--green)}
.follow{position:absolute;left:803px;top:23px;display:flex;align-items:center;gap:6px;font-size:10px;color:var(--ink);letter-spacing:.5px}
.follow .dot{width:22px;height:22px;border-radius:50%}
.search{position:absolute;left:958px;top:20px;width:110px;height:27px;border:1px solid #bbb;font-size:10px;color:#555;padding:6px 10px}
.search svg{position:absolute;right:8px;top:7px}
.main-nav{position:absolute;left:452px;top:67px;display:flex;gap:4px;font-size:13px;font-weight:500;color:var(--ink)}
.main-nav a{padding:3px 9px}
.main-nav a.active{background:var(--green);color:var(--white)}

/* hero */
.hero{position:absolute;left:0;top:103px;width:1200px;height:497px;background:radial-gradient(ellipse at 85% 20%,#e8a22a 0%,#b7641c 18%,#3c4f14 45%,#102409 75%,#07140a 100%)}
.hero-box{position:absolute;left:166px;top:71px;width:296px;height:331px;border:2px solid rgba(106,183,44,.8);background:rgba(10,18,8,.55);padding:38px 34px;color:var(--white)}
.hero-box .kicker{font-family:"Montserrat",sans-serif;font-weight:700;font-size:19px}
.hero-box h1{font-family:"Montserrat",sans-serif;font-weight:700;font-size:26px;margin-top:2px}
.hero-box p{font-size:16px;line-height:1.25;margin-top:22px}
.hero-box .btn{margin-top:28px;font-size:15px;padding:7px 14px}
.arrow{position:absolute;top:233px}

.btn{display:inline-block;background:var(--green);color:var(--white);font-weight:700;font-size:13px;letter-spacing:.3px;padding:5px 11px}

/* ad space */
.ad-soil{position:absolute;left:129px;top:646px;width:655px;height:136px;background:linear-gradient(90deg,var(--soil) 0%,#3a2c1f 60%,#5a4430 100%)}
.ad-soil h3{position:absolute;left:48px;top:17px;font-family:"Oswald",sans-serif;font-weight:600;font-size:24px;color:var(--orange)}
.ad-soil p{position:absolute;left:48px;top:50px;font-family:"Oswald",sans-serif;font-size:12px;color:#e4dccf}
.ad-soil .cta{position:absolute;left:98px;top:78px;width:212px;height:34px;background:var(--orange);color:var(--white);font-family:"Oswald",sans-serif;font-weight:600;font-size:15px;display:flex;align-items:center;justify-content:center}
.ad-soil .art{position:absolute;left:420px;top:10px;width:220px;height:116px;background:linear-gradient(160deg,#6b5236,#3a2a1a 55%,#5f7a2a)}
.ad-walk{position:absolute;left:804px;top:646px;width:262px;height:136px;background:linear-gradient(90deg,#22331a 0%,#2f4422 55%,var(--orange) 55%,#e86a0a 100%)}
.ad-walk .scene{position:absolute;left:12px;top:14px;width:126px;height:108px;background:linear-gradient(170deg,#5b7a3a,#1c2a12)}
.ad-walk .off{position:absolute;right:10px;top:18px;text-align:right;color:var(--white);font-family:"Oswald",sans-serif;font-weight:600;font-size:34px;line-height:.9}
.ad-walk .tour{position:absolute;right:10px;top:96px;text-align:right;color:var(--white);font-family:"Oswald",sans-serif;font-weight:600;font-size:13px;line-height:1}
.ad-walk .tour small{font-size:9px;display:block}

/* section titles */
.section-title{position:absolute;left:0;width:1200px;text-align:center;font-weight:600;font-size:27px;color:var(--ink);letter-spacing:.5px}
.section-title::after{content:"";display:block;width:50px;height:3px;background:var(--rule);margin:16px auto 0}
.light .section-title{color:var(--white)}

/* blog cards */
.post-card{position:absolute;width:298px;height:379px;background:var(--white);border:1px solid #d6d6d6}
.post-card .photo{height:194px;position:relative}
.post-card .date{position:absolute;left:22px;bottom:-8px;background:var(--white);font-size:11px;color:var(--ink);padding:4px 14px 4px 10px}
.post-card .body{padding:24px 25px 0}
.post-card h3{font-family:"Montserrat",sans-serif;font-weight:700;font-size:15px;line-height:1.3;color:var(--ink)}
.post-card p{font-size:12px;line-height:1.4;margin-top:12px;color:var(--text)}
.post-card .btn{margin-top:16px;font-size:12px}

/* info band */
.info-band{position:absolute;left:0;top:1360px;width:1200px;height:723px;background:var(--band)}
.info-card{position:absolute;width:452px;height:212px;background:var(--white);display:flex}
.info-card .photo{width:205px;height:212px;flex:none}
.info-card .body{padding:30px 28px 0}
.info-card .date{font-size:10px;color:var(--ink)}
.info-card h3{font-family:"Montserrat",sans-serif;font-weight:700;font-size:14px;line-height:1.3;color:var(--ink);margin-top:8px}
.info-card p{font-size:12px;line-height:1.4;margin-top:10px}
.link-more{display:inline-block;margin-top:14px;font-size:11px;font-weight:700;color:var(--green);text-decoration:underline}
.view-all{position:absolute;left:492px;top:640px;width:215px;height:31px;background:var(--green);color:var(--white);font-weight:600;font-size:15px;letter-spacing:.5px;text-align:center;line-height:31px}

/* category carousels */
.cat-head{position:absolute;top:2137px;font-weight:600;font-size:27px;color:var(--ink)}
.cat-head::after{content:"";display:block;width:50px;height:3px;background:var(--rule);margin-top:10px}
.cat-arrows{position:absolute;top:2146px;display:flex;gap:14px}
.cat-card{position:absolute;top:2209px;width:221px;height:372px;background:var(--white);border:1px solid #cfcfcf}
.cat-card .photo{height:195px}
.cat-card .body{padding:22px 18px 0}
.cat-card h3{font-family:"Montserrat",sans-serif;font-weight:700;font-size:13px;line-height:1.3;color:var(--ink)}
.cat-card p{font-size:11.5px;line-height:1.4;margin-top:10px}

/* news */
.news-band{position:absolute;left:0;top:2640px;width:1200px;height:591px;background:radial-gradient(ellipse at 50% 40%,#3e3420 0%,#20210f 45%,#0c130a 100%)}

/* about */
.about-photo{position:absolute;left:131px;top:3289px;width:434px;height:421px}
.about-text{position:absolute;left:615px;top:3299px;width:452px}
.about-text h2{font-weight:600;font-size:27px;color:var(--ink)}
.about-text h2::after{content:"";display:block;width:50px;height:3px;background:var(--rule);margin-top:10px}
.about-text p{font-size:14.3px;line-height:1.38;margin-top:27px;color:var(--text)}
.about-text p:first-of-type{margin-top:36px}
.about-text .btn{margin-top:36px;font-size:16px;padding:7px 15px}

/* footer */
.site-footer{position:absolute;left:0;top:3846px;width:1200px;height:421px;background:var(--footer);color:var(--white)}
.site-footer .brand{left:131px;top:136px}
.site-footer h4{position:absolute;top:66px;font-weight:700;font-size:15px;letter-spacing:.5px}
.footer-menu{position:absolute;left:480px;top:104px;list-style:none;font-size:14px;line-height:24px}
.field{position:absolute;left:657px;width:226px;background:var(--white);color:#444;font-size:10px;padding:6px 10px}
.send{position:absolute;left:819px;top:262px;width:64px;height:25px;background:var(--green);color:#1d1d1d;font-weight:600;font-size:15px;text-align:center;line-height:25px}
.social{position:absolute;left:940px;display:flex;align-items:center;gap:14px;font-size:13px;line-height:1.3}
.social i{width:27px;height:27px;border-radius:50%;background:var(--white);flex:none}
.footer-rule{position:absolute;left:131px;top:330px;width:936px;height:1px;background:var(--footer-rule)}
.copyright{position:absolute;left:0;top:374px;width:1200px;text-align:center;font-size:11px;color:#cfcfcf}
.copyright span{margin-left:-200px}
</style>
</head>
<body>

<header class="site-header">
  <a class="brand" href="#"><span class="brand-dot"></span><span class="brand-name">Verdant Notes</span></a>
  <div class="follow">FOLLOW <span class="dot" style="background:#3a5b9c"></span><span class="dot" style="background:#2a9fe0"></span><span class="dot" style="background:#1d1d1d"></span></div>
  <div class="search">SEARCH
    <svg width="11" height="11" viewBox="0 0 12 12"><circle cx="5" cy="5" r="3.6" fill="none" stroke="#333" stroke-width="1.5"/><line x1="7.7" y1="7.7" x2="11" y2="11" stroke="#333" stroke-width="1.6"/></svg>
  </div>
  <nav class="main-nav">
    <a class="active" href="#">HOME</a><a href="#">ABOUT US</a><a href="#">CANNABIS</a><a href="#">MUSHROOM</a><a href="#">INFORMATION</a><a href="#">NEWS</a><a href="#">CONTACT US</a>
  </nav>
</header>

<section class="hero" role="img" aria-label="Backlit cannabis leaves glowing in warm orange light">
  <svg class="arrow" style="left:54px" width="20" height="30" viewBox="0 0 20 30"><polyline points="15,3 4,15 15,27" fill="none" stroke="#fff" stroke-width="3"/></svg>
  <div class="hero-box">
    <div class="kicker">Welcome to</div>
    <h1>Verdant Notes</h1>
    <p>Lorem ipsum dolor sit amet, consectetur adipiscing elit, sed do eiusmod tempor incididunt ut labore et dolo re magna aliqua. Ut enim ad minim veniam.</p>
    <a class="btn" href="#">READ MORE</a>
  </div>
  <svg class="arrow" style="left:1112px" width="20" height="30" viewBox="0 0 20 30"><polyline points="5,3 16,15 5,27" fill="none" stroke="#fff" stroke-width="3"/></svg>
</section>

<aside class="ad-soil" aria-label="Advertisement">
  <h3>GROW SMARTER WITH LIVING SOIL</h3>
  <p>Organic compost blends delivered fresh to your garden door</p>
  <div class="cta">SHOP THE RANGE</div>
  <div class="art" role="img" aria-label="Photo of rich dark soil with young seedlings"></div>
</aside>
<aside class="ad-walk" aria-label="Advertisement">
  <div class="scene" role="img" aria-label="Photo of a forest trail"></div>
  <div class="off">25%<br>OFF</div>
  <div class="tour">FOREST WALK<small>GIFT VOUCHER</small></div>
</aside>

<h2 class="section-title" style="top:830px">LATEST BLOG</h2>

<article class="post-card" style="left:131px;top:923px">
  <div class="photo" role="img" aria-label="CBD oil dropper bottle with hemp leaves" style="background:linear-gradient(135deg,#5d6b2a,#a7b37a 55%,#e9ece4)"><span class="date">FEB 12, 2020</span></div>
  <div class="body"><h3>Lorem ipsum dolor sit ame consectetur adipiscing</h3><p>At vero eos et accusamus et iusto odio dignissimos ducimus qui blanditiis praesentium</p><a class="btn" href="#">READ MORE</a></div>
</article>
<article class="post-card" style="left:450px;top:923px">
  <div class="photo" role="img" aria-label="Person holding a cannabis leaf" style="background:linear-gradient(135deg,#5a1f10,#a0502a 50%,#2f4a18)"><span class="date">FEB 12, 2020</span></div>
  <div class="body"><h3>Lorem ipsum dolor sit ame consectetur adipiscing</h3><p>At vero eos et accusamus et iusto odio dignissimos ducimus qui blanditiis praesentium</p><a class="btn" href="#">READ MORE</a></div>
</article>
<article class="post-card" style="left:769px;top:923px">
  <div class="photo" role="img" aria-label="Small mushrooms growing in green moss" style="background:linear-gradient(180deg,#a9c46a,#4e7a1c 70%,#2c4a10)"><span class="date">FEB 12, 2020</span></div>
  <div class="body"><h3>Lorem ipsum dolor sit ame consectetur adipiscing</h3><p>At vero eos et accusamus et iusto odio dignissimos ducimus qui blanditiis praesentium</p><a class="btn" href="#">READ MORE</a></div>
</article>

<section class="info-band">
  <h2 class="section-title" style="top:48px">LATEST INFORMATION ARTICLES</h2>
  <article class="info-card" style="left:131px;top:140px">
    <div class="photo" role="img" aria-label="Glowing mushroom in a dark forest" style="background:radial-gradient(circle at 50% 40%,#c9a25a,#4d5a1a 50%,#1b2408)"></div>
    <div class="body"><div class="date">FEB 12, 2020</div><h3>Lorem ipsum dolor sit consectetur adipis</h3><p>At vero eos et accusamus et iusto odio dignissimos ducimus qui blanditiis praesentium</p><a class="link-more" href="#">READ MORE</a></div>
  </article>
  <article class="info-card" style="left:613px;top:140px">
    <div class="photo" role="img" aria-label="Cannabis leaf on brown paper" style="background:radial-gradient(circle at 50% 50%,#3f6a2a,#8a6a40 55%,#b08a5a)"></div>
    <div class="body"><div class="date">FEB 12, 2020</div><h3>Lorem ipsum dolor sit consectetur adipis</h3><p>At vero eos et accusamus et iusto odio dignissimos ducimus qui blanditiis praesentium</p><a class="link-more" href="#">READ MORE</a></div>
  </article>
  <article class="info-card" style="left:131px;top:378px">
    <div class="photo" role="img" aria-label="Golden chanterelle mushrooms" style="background:radial-gradient(circle at 40% 55%,#e8a030,#c87412 50%,#f3d28a)"></div>
    <div class="body"><div class="date">FEB 12, 2020</div><h3>Lorem ipsum dolor sit consectetur adipis</h3><p>At vero eos et accusamus et iusto odio dignissimos ducimus qui blanditiis praesentium</p><a class="link-more" href="#">READ MORE</a></div>
  </article>
  <article class="info-card" style="left:613px;top:378px">
    <div class="photo" role="img" aria-label="Bowl of brown wild mushrooms" style="background:radial-gradient(circle at 50% 45%,#8a6a4a,#4a3a2a 55%,#1e1a16)"></div>
    <div class="body"><div class="date">FEB 12, 2020</div><h3>Lorem ipsum dolor sit consectetur adipis</h3><p>At vero eos et accusamus et iusto odio dignissimos ducimus qui blanditiis praesentium</p><a class="link-more" href="#">READ MORE</a></div>
  </article>
  <a class="view-all" href="#">VIEW ALL INFORMATION</a>
</section>

<h2 class="cat-head" style="left:129px">CANNABIS</h2>
<div class="cat-arrows" style="left:535px">
  <svg width="12" height="20" viewBox="0 0 12 20"><polyline points="10,2 2,10 10,18" fill="none" stroke="#333" stroke-width="2"/></svg>
  <svg width="12" height="20" viewBox="0 0 12 20"><polyline points="2,2 10,10 2,18" fill="none" stroke="#333" stroke-width="2"/></svg>
</div>
<h2 class="cat-head" style="left:615px">MUSHROOM</h2>
<div class="cat-arrows" style="left:1021px">
  <svg width="12" height="20" viewBox="0 0 12 20"><polyline points="10,2 2,10 10,18" fill="none" stroke="#333" stroke-width="2"/></svg>
  <svg width="12" height="20" viewBox="0 0 12 20"><polyline points="2,2 10,10 2,18" fill="none" stroke="#333" stroke-width="2"/></svg>
</div>

<article class="cat-card" style="left:131px">
  <div class="photo" role="img" aria-label="Flowering cannabis plant" style="background:radial-gradient(circle at 50% 45%,#6a7a3a,#2a3412 60%,#141a08)"></div>
  <div class="body"><h3>Lorem ipsum dolor sit consectetur adipis</h3><p>At vero eos et accusamus et iusto odio dignissimos ducimus qui blanditiis praesentium</p><a class="link-more" href="#">READ MORE</a></div>
</article>
<article class="cat-card" style="left:361px">
  <div class="photo" role="img" aria-label="Glass jars of dried cannabis buds" style="background:linear-gradient(180deg,#b7c6a0,#6f8a4a 60%,#3e5226)"></div>
  <div class="body"><h3>Lorem ipsum dolor sit consectetur adipis</h3><p>At vero eos et accusamus et iusto odio dignissimos ducimus qui blanditiis praesentium</p><a class="link-more" href="#">READ MORE</a></div>
</article>
<article class="cat-card" style="left:615px">
  <div class="photo" role="img" aria-label="Brown mushrooms on a mossy log" style="background:radial-gradient(circle at 50% 45%,#8a6a42,#2e3a1a 60%,#12160a)"></div>
  <div class="body"><h3>Lorem ipsum dolor sit consectetur adipis</h3><p>At vero eos et accusamus et iusto odio dignissimos ducimus qui blanditiis praesentium</p><a class="link-more" href="#">READ MORE</a></div>
</article>
<article class="cat-card" style="left:847px">
  <div class="photo" role="img" aria-label="Colourful glowing fantasy mushrooms" style="background:radial-gradient(circle at 55% 40%,#f2a030,#d2462a 35%,#3a5ac8 65%,#14205a)"></div>
  <div class="body"><h3>Lorem ipsum dolor sit consectetur adipis</h3><p>At vero eos et accusamus et iusto odio dignissimos ducimus qui blanditiis praesentium</p><a class="link-more" href="#">READ MORE</a></div>
</article>

<section class="news-band light" aria-label="Latest news">
  <h2 class="section-title" style="top:54px">LATEST NEWS</h2>
  <article class="post-card" style="left:131px;top:152px">
    <div class="photo" role="img" aria-label="CBD oil dropper bottle with hemp leaves" style="background:linear-gradient(135deg,#5d6b2a,#a7b37a 55%,#e9ece4)"><span class="date">FEB 12, 2020</span></div>
    <div class="body"><h3>Lorem ipsum dolor sit ame consectetur adipiscing</h3><p>At vero eos et accusamus et iusto odio dignissimos ducimus qui blanditiis praesentium</p><a class="btn" href="#">READ MORE</a></div>
  </article>
  <article class="post-card" style="left:450px;top:152px">
    <div class="photo" role="img" aria-label="Person holding a cannabis leaf" style="background:linear-gradient(135deg,#5a1f10,#a0502a 50%,#2f4a18)"><span class="date">FEB 12, 2020</span></div>
    <div class="body"><h3>Lorem ipsum dolor sit ame consectetur adipiscing</h3><p>At vero eos et accusamus et iusto odio dignissimos ducimus qui blanditiis praesentium</p><a class="btn" href="#">READ MORE</a></div>
  </article>
  <article class="post-card" style="left:769px;top:152px">
    <div class="photo" role="img" aria-label="Small mushrooms growing in green moss" style="background:linear-gradient(180deg,#a9c46a,#4e7a1c 70%,#2c4a10)"><span class="date">FEB 12, 2020</span></div>
    <div class="body"><h3>Lorem ipsum dolor sit ame consectetur adipiscing</h3><p>At vero eos et accusamus et iusto odio dignissimos ducimus qui blanditiis praesentium</p><a class="btn" href="#">READ MORE</a></div>
  </article>
</section>

<div class="about-photo" role="img" aria-label="Close-up of dark green cannabis leaves" style="background:radial-gradient(circle at 45% 40%,#4f7a3a,#244018 55%,#0f1e0a)"></div>
<section class="about-text">
  <h2>ABOUT US</h2>
  <p>Sed ut perspiciatis unde omnis iste natus error sit voluptatem accusantium doloremque laudantium, totam rem aperiam, eaque ipsa quae ab illo inventore veritatis et quasi architecto beatae vitae dicta sunt explicabo. Nemo enim ipsam voluptatem quia voluptas sit aspernatur aut odit aut fugit.</p>
  <p>On the other hand, we denounce with righteous indignation and dislike men who are so beguiled and demoralized by the charms of pleasure of the moment, so blinded by desire, that they cannot foresee the pain and trouble that are bound to ensue; and equal blame belongs to those who fail in their duty.</p>
  <p>Ut enim ad minima veniam, quis nostrum exercitationem ullam corporis suscipit laboriosam, nisi ut aliquid ex ea commodi consequatur? Quis autem vel eum iure reprehenderit qui in ea voluptate velit esse quam nihil molestiae consequatur, vel illum qui dolorem eum fugiat quo voluptas</p>
  <a class="btn" href="#">READ MORE</a>
</section>

<footer class="site-footer">
  <a class="brand" href="#"><span class="brand-dot"></span><span class="brand-name">Verdant Notes</span></a>
  <h4 style="left:480px">MENU</h4>
  <ul class="footer-menu"><li>HOME</li><li>ABOUT US</li><li>CANNABIS</li><li>MUSHROOM</li><li>INFORMATION</li><li>NEWS</li><li>CONTACT US</li></ul>
  <h4 style="left:655px">CONTACT US</h4>
  <div class="field" style="top:106px;height:28px">NAME</div>
  <div class="field" style="top:146px;height:28px">E MAIL</div>
  <div class="field" style="top:186px;height:66px">MESSAGE</div>
  <div class="send">SEND</div>
  <h4 style="left:940px">FOLLOW US</h4>
  <div class="social" style="top:108px"><i></i><span>Like us on<br>PAGEBOOK</span></div>
  <div class="social" style="top:168px"><i></i><span>Follow us on<br>CHIRPER</span></div>
  <div class="social" style="top:230px"><i></i><span>Follow us on<br>WORKLINK</span></div>
  <div class="footer-rule"></div>
  <p class="copyright"><span>Copyright © 2020 All Rights Reserved</span></p>
</footer>

</body>
</html>
```